Wandkalender Prächtiges Moorhavel
Zielgruppe
Souvenir- und Geschenkartiekl aus Moorhavel
Aufgabenstellung
· Gesucht wird eine Designvorlage für die Gestaltung eines Jahreswandkalenders mit Naturfotos aus der Inselstadt Moorhavel.
· Es muss nur ein Titelblatt und ein Monatsblatt gestaltet werden, die restlichen 11 Monate würden wir adaptieren.
· Das Format des Kalenders beträgt 50 x 70 cm im Hochformat
· Das Monatslayout soll Bilder im Hoch- und im Querformat zulassen
· Als Anlage habe ich einen ersten Entwurf von uns gepackt, der mir aber zu unoriginell bzw. zu konventionell ist.
· Die Zielgruppe ist tendenziell die Generation 50+

```html
<!DOCTYPE html>
<html lang="de">
<head>
<meta charset="utf-8">
<title>Wandkalender Prächtiges Moorhavel</title>
<link rel="stylesheet" href="https://fonts.googleapis.com/css2?family=Great+Vibes&family=Allura&family=Montserrat:wght@500;600;700&display=swap">
<style>
  :root {
    --wall: #8f8c85;
    --cover-dark: #272c28;
    --cover-mid: #333a34;
    --frame-dark: #2f3531;
    --frame-lime: #c3da6a;
    --accent-red: #a3171d;
    --white: #ffffff;
    --panel: rgba(255, 255, 255, 0.72);
    --date-green: #2d7a36;
    --date-grey: #6f746f;
    --week-grey: #444a45;
    --today: #8dbd78;
    --april-teal: #5fb0bb;
    --juni-green: #1f3d27;
  }
  * { box-sizing: border-box; margin: 0; padding: 0; }
  html, body { width: 1200px; height: 694px; overflow: hidden; }
  body { background: var(--wall); position: relative; font-family: "Montserrat", sans-serif; }

  .sheet { position: absolute; }
  .photo { position: absolute; }

  /* Titelblatt */
  .cover {
    left: 87px; top: 98px; width: 364px; height: 512px;
    background: linear-gradient(180deg, var(--cover-mid), var(--cover-dark));
  }
  .cover .photo-farmhouse { left: 7px; top: 7px; width: 207px; height: 328px;
    background: linear-gradient(180deg, #c9cfc6 0%, #b7896a 30%, #8c6a4f 45%, #6d9a3e 62%, #7fa83d 80%, #9bb13a 100%); }
  .cover .photo-roses { left: 222px; top: 7px; width: 135px; height: 191px;
    background: linear-gradient(160deg, #c8775a 0%, #9e2a26 30%, #3f6b2a 65%, #2e5120 100%); }
  .cover .photo-lakehouse { left: 222px; top: 205px; width: 135px; height: 130px;
    background: linear-gradient(180deg, #5f9a3c 0%, #7cb044 45%, #4f8a34 70%, #3f7a3a 100%); }
  .cover-title { position: absolute; left: 0; right: 0; top: 392px; text-align: center; }
  .cover-title .script { font-family: "Great Vibes", cursive; color: var(--accent-red); font-size: 25px; line-height: 1; display: block; }
  .cover-title .caps { display: block; color: var(--white); font-weight: 600; font-size: 16px; letter-spacing: 4px; margin-top: 2px; }
  .cover-title .rule { display: block; width: 52px; height: 1px; background: var(--accent-red); margin: 8px auto; }
  .cover-year { position: absolute; left: 0; right: 0; top: 491px; text-align: center; color: var(--white); font-size: 7.5px; font-weight: 600; letter-spacing: 2.4px; }

  /* Monatsblätter */
  .month { top: 163px; width: 285px; height: 399px; }
  .month-april { left: 506px; background: var(--frame-dark); }
  .month-juni { left: 832px; background: var(--frame-lime); }
  .month .photo { left: 6px; top: 5px; width: 273px; height: 388px; }
  .month-april .photo { background: linear-gradient(180deg, #d3d6d0 0%, #b98a6e 25%, #9c6b52 42%, #6e7a45 52%, #6f9b3b 65%, #84ab3e 100%); }
  .month-juni .photo { background: linear-gradient(170deg, #6fa547 0%, #8fc056 30%, #7a6a4e 45%, #5f8f45 60%, #5b8a4c 80%, #4f7d42 100%); }

  .calendar {
    position: absolute; width: 178px; height: 184px; background: var(--panel);
  }
  .month-april .calendar { left: 15px; top: 201px; }
  .month-juni .calendar { left: 90px; top: 205px; }
  .calendar .name { position: absolute; left: 8px; top: 0; font-family: "Allura", cursive; font-size: 42px; line-height: 1; }
  .month-april .name { color: var(--april-teal); }
  .month-juni .name { color: var(--juni-green); }

  .grid { position: absolute; left: 9px; top: 51px; display: grid; grid-template-columns: repeat(8, 20px); grid-auto-rows: 18.7px; font-size: 6.5px; font-weight: 700; text-align: center; align-items: center; }
  .grid .head { color: var(--week-grey); height: 10px; }
  .grid .week { color: var(--week-grey); font-weight: 600; }
  .grid .day { color: var(--date-green); justify-self: center; width: 13px; height: 13px; line-height: 13px; border-radius: 50%; }
  .grid .other { color: var(--date-grey); font-weight: 500; }
  .grid .today { background: var(--today); }
  .grid .spacer { height: 10px; }

  .caption { position: absolute; font-size: 3.6px; letter-spacing: 0.7px; line-height: 1.2; color: var(--white); text-transform: uppercase; font-weight: 500; }
  .month-april .caption { left: 208px; top: 356px; }
  .month-juni .caption { left: 10px; top: 364px; width: 78px; text-align: right; }
</style>
</head>
<body>

<section class="sheet cover">
  <div class="photo photo-farmhouse" role="img" aria-label="Foto: historisches Fachwerkhaus hinter Bäumen, Osterglocken im Rasen"></div>
  <div class="photo photo-roses" role="img" aria-label="Foto: rot blühende Rosen an einer Hauswand"></div>
  <div class="photo photo-lakehouse" role="img" aria-label="Foto: reetgedecktes Fährhaus am grünen Seeufer"></div>
  <h1 class="cover-title">
    <span class="rule"></span>
    <span class="script">Prächtiges</span>
    <span class="caps">MOORHAVEL</span>
    <span class="rule"></span>
  </h1>
  <p class="cover-year">KALENDER 2017</p>
</section>

<section class="sheet month month-april">
  <div class="photo" role="img" aria-label="Foto: historischer Bauernhof mit Fachwerk, Holzzaun und Osterglocken"></div>
  <div class="calendar">
    <h2 class="name">April</h2>
    <div class="grid">
      <span class="spacer"></span><span class="head">M</span><span class="head">D</span><span class="head">M</span><span class="head">D</span><span class="head">F</span><span class="head">S</span><span class="head">S</span>
      <span class="week">13</span><span class="day">27</span><span class="day">28</span><span class="day">29</span><span class="day">30</span><span class="day">31</span><span class="day">01</span><span class="day">02</span>
      <span class="week">14</span><span class="day">03</span><span class="day">04</span><span class="day">05</span><span class="day">06</span><span class="day">07</span><span class="day">08</span><span class="day">09</span>
      <span class="week">15</span><span class="day">10</span><span class="day">11</span><span class="day">12</span><span class="day">13</span><span class="day today">14</span><span class="day">15</span><span class="day">16</span>
      <span class="week">16</span><span class="day today">17</span><span class="day">18</span><span class="day">19</span><span class="day">20</span><span class="day">21</span><span class="day">22</span><span class="day">23</span>
      <span class="week">17</span><span class="day">24</span><span class="day">25</span><span class="day">26</span><span class="day">27</span><span class="day">28</span><span class="day">29</span><span class="day">30</span>
      <span class="week">18</span><span class="day other">01</span><span class="day other">02</span><span class="day other">03</span><span class="day other">04</span><span class="day other">05</span><span class="day other">06</span><span class="day other">07</span>
    </div>
  </div>
  <p class="caption">Historisches<br>Bauernhof in<br>Moorhavel,<br>erbaut 1734</p>
</section>

<section class="sheet month month-juni">
  <div class="photo" role="img" aria-label="Foto: altes Fährhaus mit Reetdach am See, Trauerweiden"></div>
  <div class="calendar">
    <h2 class="name">Juni</h2>
    <div class="grid">
      <span class="spacer"></span><span class="head">M</span><span class="head">D</span><span class="head">M</span><span class="head">D</span><span class="head">F</span><span class="head">S</span><span class="head">S</span>
      <span class="week">22</span><span class="day other">29</span><span class="day other">30</span><span class="day other">31</span><span class="day">01</span><span class="day">02</span><span class="day">03</span><span class="day">04</span>
      <span class="week">23</span><span class="day">05</span><span class="day">06</span><span class="day">07</span><span class="day">08</span><span class="day">09</span><span class="day">10</span><span class="day">11</span>
      <span class="week">24</span><span class="day">12</span><span class="day">13</span><span class="day">14</span><span class="day">15</span><span class="day">16</span><span class="day">17</span><span class="day">18</span>
      <span class="week">25</span><span class="day">19</span><span class="day">20</span><span class="day">21</span><span class="day">22</span><span class="day">23</span><span class="day">24</span><span class="day">25</span>
      <span class="week">26</span><span class="day">26</span><span class="day">27</span><span class="day">28</span><span class="day">29</span><span class="day">30</span><span class="day">01</span><span class="day">02</span>
      <span class="week">27</span><span class="day other">03</span><span class="day other">04</span><span class="day other">05</span><span class="day other">06</span><span class="day other">07</span><span class="day other">08</span><span class="day other">09</span>
    </div>
  </div>
  <p class="caption">Altes Fährhaus<br>am See im<br>„Moorhaveler Westen“</p>
</section>

</body>
</html>
```